Etiketten für Tees
Zielgruppe
Wir sind eine klassische Foto-Drogerie mit traditioneller Likör Herstellung, Tee- und Gewürzstube mit offenen und selbst abgepackten Spezialitäten. Süßwarenabteilung mit Confiserie, großer Bonbon Auswahl und Drogerie Grundsortiment.
Wir suchen ein neues Etiketten Design für unsere selbst abgepackten Tees, Bonbons und Gewürze.
Aufgabenstellung
Die Etiketten für die Tees sollten durch verschiedene Farben oder Grafiken in die nachfolgenden Kategorien unterscheidbar sein: Schwarzer Tee, Grüner Tee, Früchte Tee, Rooibusch Tee und Kräuter Tee.
Abgefüllt sind die Tees in Blockbeutel Natron natur und die Früchtetees in Klarsichtbeutel.
Die Etiketten sollten etwa 65mm breit sein. die Länge kann zwischen 70mm und 110mm betragen.
Folgene Information müsste aufgedruckt werden: Art (Schwarzer Tee), Sorte (Darjeeling), kurze Beschreibung oder Geschmack (Erdbeer Geschmack), Füllmenge sowie unser Logo mit Adresse. Die Inhaltsstoffe, Zubereitung, Nährwerttabelle kommen in Text oder Tabellenform auf die Rückseite auf ein neutrales Etikett (hier nicht zu berücksichtigen).
Die Etiketten wollen wir mit unserem hochwertigen Vollfarb Etikettendrucker selbst ausdrucken (Drucker Velantis).
Das Design sollte auf die Natron Beutel farblich und von der Gestaltung her abgestimmt sein (natürliches und qualitativ hochwertiges Produkt - keine Massenware vom Discounter, jedoch trotzdem modern und 'nicht angestaubt spießig', aber nicht zu grelle Farben).
Wir möchten diese Etiketten im Sinne eines stimmigen Gesamtauftritts (sh. Foto) auch für unsere selbst abgepackten Bonbons und Gewürze verwenden. Es unterscheidet sich also nur marginal, d.h. in Bezeichnung und Füllmenge. Logo und Adresse bzw. das Gesamtbild sollen also gleich sein.

```html
<!DOCTYPE html>
<html lang="de">
<head>
<meta charset="utf-8">
<title>Teestube Lindmoor – Schwarzer Tee Darjeeling</title>
<link rel="stylesheet" href="https://fonts.googleapis.com/css2?family=Noticia+Text:wght@400&family=Roboto+Condensed:wght@300;400;700&display=swap">
<style>
  :root {
    --paper: #ffffff;
    --ink: #1f1a17;
    --tea-green: #145a32;
    --gold-light: #fbeec0;
    --gold-mid: #e9c35a;
    --gold-deep: #b98a2a;
    --panel: rgba(255, 253, 244, 0.86);
  }
  * { margin: 0; padding: 0; box-sizing: border-box; }
  html, body {
    width: 1029px;
    height: 1200px;
    overflow: hidden;
    background: var(--paper);
  }
  .label {
    position: relative;
    width: 1029px;
    height: 1200px;
    background: var(--paper);
    font-family: "Roboto Condensed", "Arial Narrow", sans-serif;
    color: var(--ink);
  }
  .gold-texture {
    position: absolute;
    inset: 0;
    width: 1029px;
    height: 1200px;
  }
  .brand {
    position: absolute;
    top: 150px;
    left: 0;
    width: 1029px;
    display: flex;
    justify-content: center;
    align-items: center;
    gap: 22px;
  }
  .brand-name {
    font-family: "Noticia Text", Georgia, serif;
    font-weight: 400;
    font-size: 66px;
    line-height: 1;
    color: var(--ink);
  }
  .brand-dot {
    width: 46px;
    height: 46px;
    border-radius: 50%;
    background: var(--ink);
  }
  .info-panel {
    position: absolute;
    left: 184px;
    top: 355px;
    width: 703px;
    height: 567px;
    border-radius: 11px;
    background: var(--panel);
  }
  .category {
    position: absolute;
    top: 418px;
    left: 184px;
    width: 703px;
    text-align: center;
    font-weight: 300;
    font-size: 56px;
    letter-spacing: 6px;
    line-height: 1;
    color: var(--ink);
  }
  .divider {
    position: absolute;
    top: 505px;
    left: 214px;
    width: 744px;
    border-top: 3px dotted var(--ink);
  }
  .variety {
    position: absolute;
    top: 520px;
    left: 184px;
    width: 703px;
    text-align: center;
    font-family: "Noticia Text", Georgia, serif;
    font-size: 88px;
    line-height: 1.1;
    color: var(--tea-green);
  }
  .description {
    position: absolute;
    top: 680px;
    left: 184px;
    width: 703px;
    text-align: center;
    font-size: 27px;
    line-height: 40px;
    color: var(--ink);
  }
  .net-weight {
    position: absolute;
    top: 950px;
    left: 0;
    width: 1029px;
    text-align: center;
    font-weight: 700;
    font-size: 60px;
    line-height: 1;
    color: var(--tea-green);
  }
</style>
</head>
<body>
<main class="label">
  <svg class="gold-texture" viewBox="0 0 1029 1200" role="img" aria-label="Goldene Pinselstrich-Textur als Hintergrund">
    <defs>
      <linearGradient id="goldSweep" x1="0" y1="0" x2="1" y2="1">
        <stop offset="0" stop-color="var(--gold-light)"/>
        <stop offset="0.3" stop-color="var(--gold-mid)"/>
        <stop offset="0.55" stop-color="var(--gold-light)"/>
        <stop offset="0.8" stop-color="var(--gold-deep)"/>
        <stop offset="1" stop-color="var(--gold-mid)"/>
      </linearGradient>
    </defs>
    <path fill="url(#goldSweep)" d="M120 120 C260 40 520 20 720 70 C860 110 960 160 1000 280 C1029 420 990 560 1010 700 C1020 820 940 930 880 1040 C820 1130 700 1190 560 1180 C420 1175 300 1140 250 1060 C170 980 60 940 40 820 C20 700 10 560 50 420 C70 300 40 200 120 120 Z"/>
  </svg>

  <header class="brand">
    <span class="brand-name">Teestube Lindmoor</span>
    <span class="brand-dot"></span>
  </header>

  <div class="info-panel"></div>
  <p class="category">SCHWARZER TEE</p>
  <div class="divider"></div>
  <h1 class="variety">Darjeeling</h1>
  <p class="description">Eine Teesorte aus dem indischen Distrikt<br>Darjeeling. Ein weitfermentierter Tee, der<br>Eigenschaften von Oolong und Schwarztee<br>in sich vereint.</p>
  <p class="net-weight">100 g</p>
</main>
</body>
</html>
```